Product Label Design for Natural Cosmetics brand

For our company Solmirena, we are looking for a completely new label design for our natural cosmetics line made with Organic Aloe Vera.
The first product in line is Travessa, our Aloe Vera Gel. Based on the schema you create, further labels would have to be created.
Since the line includes different products (for Face, Body, Hands, Sun), there should be some color distinction between different product that can keep the products apart, having still a very similar schema.
The label should reflect the South Portuguese (Algarve) way, trust and quality. The label design should be minimalistic, well recognizable and readable, including though the following components
Logo
Product Name: Travessa (medium)
Product Function (in Portuguese mainly): GEL DE ALOÉ VERA BIO (Large and visible)
Key Infomation: For Skin and Hair
Contains 200x concentrated Aloe Vera and Organic Jojoba Oil
Following logos are to be placed on the packaging: Vegan, Organic Aloe Vera, Natural Product
Additional Info:
Barcode (EAN Number)
Ingredients (please see the current label)
Made in Portugal
Address: Check current label
QR Code for URL to open Instructions and get support
Functions and Instructions need to be in the following language:
Function: Bio Aloe Vera Gel
Instruction: External Use.
English, Spanish, French, Italian, German, Dutch, Swedish, Portuguese, Arabic
Please use google translate or put placeholders for the respective languages.
I am uploading the current label (content and design is different than what we are looking for), the package (the amber pump bottle remains the same and is available to see at https://solmirena.example/default/travessa-aloe-vera-gel-1.html ) and the logo.
We would like you to illustrate how the label would look on the bottle and how you plan to distinct between other products that we will be designing in the series.
Please let me know if you need anything else.

```html
<!DOCTYPE html>
<html lang="en">
<head>
<meta charset="utf-8">
<title>Solmirena – Travessa Gel de Aloé Vera Bio label</title>
<link rel="stylesheet" href="https://fonts.googleapis.com/css2?family=Montserrat:wght@400;500;600;700&display=swap">
<style>
  :root {
    --page-bg: #eeeeee;
    --sky-top: #78b0b6;
    --sky-mid: #a4c8c9;
    --sky-low: #d6ddd4;
    --cliff: #a8d1cf;
    --sea: #80b5b8;
    --navy: #2a2c6e;
    --navy-deep: #24265f;
    --cream: #efe7dc;
  }
  * { margin: 0; padding: 0; box-sizing: border-box; }
  html, body {
    width: 1200px;
    height: 2913px;
    overflow: hidden;
    background: var(--page-bg);
    font-family: "Montserrat", sans-serif;
  }
  .label {
    position: absolute;
    left: 113px;
    top: 1131px;
    width: 927px;
    height: 1298px;
    overflow: hidden;
    background: linear-gradient(180deg, var(--sky-top) 0%, var(--sky-mid) 30%, var(--sky-low) 55%, var(--sky-low) 62%);
  }
  .coast-scene {
    position: absolute;
    left: 0; right: 0;
    top: 760px;
    bottom: 0;
    background: linear-gradient(180deg,
      rgba(214,221,212,0) 0%,
      var(--cliff) 18%,
      var(--sea) 32%,
      #6d8db0 44%,
      var(--navy) 56%,
      var(--navy-deep) 100%);
  }
  .brand-mark {
    position: absolute;
    left: 50%;
    top: 96px;
    width: 350px;
    height: 350px;
    transform: translateX(-50%);
  }
  .brand-name {
    position: absolute;
    left: 0; right: 0;
    top: 250px;
    text-align: center;
    font-weight: 500;
    font-size: 34px;
    line-height: 42px;
    letter-spacing: 6px;
    color: var(--cream);
  }
  .product-name {
    position: absolute;
    left: 0; right: 0;
    top: 488px;
    text-align: center;
    font-weight: 500;
    font-size: 56px;
    line-height: 68px;
    letter-spacing: 4px;
    color: var(--cream);
  }
  .product-function {
    position: absolute;
    left: 0; right: 0;
    top: 556px;
    text-align: center;
    font-weight: 700;
    font-size: 60px;
    line-height: 68px;
    color: var(--navy);
  }
  .key-info {
    position: absolute;
    left: 0; right: 0;
    top: 636px;
    text-align: center;
    font-weight: 400;
    font-size: 42px;
    line-height: 52px;
    letter-spacing: 3px;
    color: var(--cream);
  }
  .ingredients-claim {
    position: absolute;
    left: 0; right: 0;
    top: 1144px;
    text-align: center;
    font-weight: 500;
    font-size: 31px;
    line-height: 52px;
    letter-spacing: 2px;
    color: var(--cream);
  }
  .net-content {
    position: absolute;
    left: 0; right: 0;
    top: 1258px;
    text-align: center;
    font-weight: 500;
    font-size: 20px;
    line-height: 26px;
    letter-spacing: 1px;
    color: var(--cream);
  }
</style>
</head>
<body>
  <section class="label">
    <div class="coast-scene" role="img" aria-label="Illustration of Algarve coastal cliffs above the sea, with dark blue aloe vera leaves in the foreground"></div>

    <svg class="brand-mark" viewBox="0 0 350 350" aria-hidden="true">
      <circle cx="175" cy="175" r="170" fill="none" stroke="var(--cream)" stroke-width="4"/>
    </svg>
    <div class="brand-name">SOLMIRENA</div>

    <h2 class="product-name">Travessa</h2>
    <h1 class="product-function">GEL DE ALOÉ VERA BIO</h1>
    <p class="key-info">For Skin and Hair</p>

    <p class="ingredients-claim">Contains 200x concentrated Aloe Vera<br>and Organic Jojoba Oil</p>
    <p class="net-content">NET WT. 300ML</p>
  </section>
</body>
</html>
```